furniture and home contents restoration

I need to list the services that we perform in our studio.
we serve the general public as well as the insurance/ remediation industry

```html
<!DOCTYPE html>
<html lang="en">
<head>
<meta charset="utf-8">
<title>Daniel Morrow – Business Cards</title>
<link rel="stylesheet" href="https://fonts.googleapis.com/css2?family=EB+Garamond:wght@400;500;600&display=swap">
<style>
  :root {
    --bg: #2b2b2d;
    --card: #f7f7f7;
    --orange: #e8742a;
    --blue: #1ea4dc;
    --ink: #4a4a4a;
    --grey: #8a8a8a;
    --faint-blue: #dbeaf1;
    --faint-peach: #f4e6dc;
    --faint-grey: #e6e6e6;
  }
  * { box-sizing: border-box; margin: 0; padding: 0; }
  html, body { width: 1200px; height: 900px; overflow: hidden; }
  body {
    background: var(--bg);
    font-family: "EB Garamond", "Palatino Linotype", serif;
    position: relative;
  }
  .card {
    position: absolute;
    width: 680px;
    height: 390px;
    background: var(--card);
    overflow: hidden;
    box-shadow: 0 10px 28px rgba(0,0,0,.45);
  }
  .card--services { left: 50px; top: 40px; }
  .card--contact { left: 470px; top: 470px; }

  .backdrop {
    position: absolute;
    border-radius: 50%;
    filter: blur(2px);
  }

  /* services side */
  .services-title {
    position: absolute; left: 34px; top: 30px;
    color: var(--orange); font-size: 27px; font-weight: 600;
  }
  .services-list, .extras-list {
    position: absolute; left: 40px; list-style: none;
    color: var(--ink); font-size: 14px; line-height: 21px;
  }
  .services-list { top: 70px; }
  .extras-list { top: 296px; }
  .services-list li, .extras-list li { display: flex; align-items: center; gap: 9px; white-space: nowrap; }
  .star { width: 12px; height: 12px; fill: var(--blue); flex: none; }
  .services-rule {
    position: absolute; left: 34px; top: 287px; width: 430px; height: 1.5px;
    background: var(--orange);
  }

  .brand { position: absolute; text-align: left; }
  .brand-row { display: flex; align-items: center; gap: 10px; }
  .brand-dot { width: 16px; height: 16px; border-radius: 50%; background: var(--blue); flex: none; }
  .brand-name {
    color: var(--blue); font-size: 24px; letter-spacing: .5px; text-transform: uppercase; white-space: nowrap;
  }
  .brand-tag {
    margin-left: 60px; color: var(--ink); font-size: 13px; letter-spacing: .6px;
    border-top: 1px solid var(--grey); padding-top: 1px; display: inline-block; white-space: nowrap;
  }
  .card--services .brand { right: 22px; top: 158px; }
  .card--services .brand-name { font-size: 20px; }
  .card--services .brand-dot { width: 14px; height: 14px; }
  .card--services .brand-tag { margin-left: 40px; font-size: 12px; }

  /* contact side */
  .holder { position: absolute; left: 34px; top: 80px; }
  .holder-name {
    color: var(--orange); font-size: 30px; font-weight: 500; text-transform: uppercase; letter-spacing: .5px;
  }
  .holder-role { color: var(--blue); font-size: 23px; font-weight: 600; margin-top: 2px; }
  .holder-note {
    color: var(--ink); font-size: 19px; line-height: 23px; margin-top: 6px; max-width: 330px;
  }
  .contact-list {
    position: absolute; left: 410px; top: 48px; list-style: none;
    color: var(--ink); font-size: 19px; line-height: 29px;
  }
  .contact-list li { display: flex; align-items: flex-start; gap: 10px; }
  .contact-icon { width: 15px; height: 15px; fill: var(--blue); margin-top: 7px; flex: none; }
  .contact-rule {
    position: absolute; left: 390px; top: 232px; width: 290px; height: 1.5px; background: var(--orange);
  }
  .card--contact .brand { left: 400px; top: 262px; }
</style>
</head>
<body>

<section class="card card--services">
  <div class="backdrop" role="img" aria-label="faint soft background tint" style="left:380px;top:-60px;width:260px;height:300px;background:var(--faint-blue);opacity:.7"></div>
  <div class="backdrop" role="img" aria-label="faint soft background tint" style="left:500px;top:-40px;width:220px;height:260px;background:var(--faint-peach);opacity:.8"></div>

  <h2 class="services-title">Our Services -</h2>
  <ul class="services-list">
    <li><svg class="star" viewBox="0 0 24 24"><path d="M12 1l3.2 7.2 7.8.7-5.9 5.2 1.8 7.7L12 17.8 5.1 21.8l1.8-7.7L1 8.9l7.8-.7z"/></svg>Antique Repair And Restoration / Metal Polishing And Restoration</li>
    <li><svg class="star" viewBox="0 0 24 24"><path d="M12 1l3.2 7.2 7.8.7-5.9 5.2 1.8 7.7L12 17.8 5.1 21.8l1.8-7.7L1 8.9l7.8-.7z"/></svg>Art Cleaning And Remounting / Odor Removal And Ozone Services</li>
    <li><svg class="star" viewBox="0 0 24 24"><path d="M12 1l3.2 7.2 7.8.7-5.9 5.2 1.8 7.7L12 17.8 5.1 21.8l1.8-7.7L1 8.9l7.8-.7z"/></svg>Art And Mirror Frame Repair / Photo Restoration</li>
    <li><svg class="star" viewBox="0 0 24 24"><path d="M12 1l3.2 7.2 7.8.7-5.9 5.2 1.8 7.7L12 17.8 5.1 21.8l1.8-7.7L1 8.9l7.8-.7z"/></svg>Chandelier Cleaning And Restoration / Upholstery Cleaning And Deodorizing</li>
    <li><svg class="star" viewBox="0 0 24 24"><path d="M12 1l3.2 7.2 7.8.7-5.9 5.2 1.8 7.7L12 17.8 5.1 21.8l1.8-7.7L1 8.9l7.8-.7z"/></svg>Document Restoration / In-house Upholstery And Reupholstery</li>
    <li><svg class="star" viewBox="0 0 24 24"><path d="M12 1l3.2 7.2 7.8.7-5.9 5.2 1.8 7.7L12 17.8 5.1 21.8l1.8-7.7L1 8.9l7.8-.7z"/></svg>Glass, Ceramic, And Mirror Repair / Rug Cleaning And Restoration</li>
    <li><svg class="star" viewBox="0 0 24 24"><path d="M12 1l3.2 7.2 7.8.7-5.9 5.2 1.8 7.7L12 17.8 5.1 21.8l1.8-7.7L1 8.9l7.8-.7z"/></svg>Hardware Repair And Restoration / Musical Instrument Restoration</li>
    <li><svg class="star" viewBox="0 0 24 24"><path d="M12 1l3.2 7.2 7.8.7-5.9 5.2 1.8 7.7L12 17.8 5.1 21.8l1.8-7.7L1 8.9l7.8-.7z"/></svg>Kitchen Removal And Reinstallation / Window Treatment Repair / Restoration</li>
    <li><svg class="star" viewBox="0 0 24 24"><path d="M12 1l3.2 7.2 7.8.7-5.9 5.2 1.8 7.7L12 17.8 5.1 21.8l1.8-7.7L1 8.9l7.8-.7z"/></svg>Lamp Cleaning And Restoration / Leather Restoration And Replacement</li>
    <li><svg class="star" viewBox="0 0 24 24"><path d="M12 1l3.2 7.2 7.8.7-5.9 5.2 1.8 7.7L12 17.8 5.1 21.8l1.8-7.7L1 8.9l7.8-.7z"/></svg>Lamp Shade Replacement / Piano Restoration And Repair</li>
  </ul>
  <div class="services-rule"></div>
  <ul class="extras-list">
    <li><svg class="star" viewBox="0 0 24 24"><path d="M12 1l3.2 7.2 7.8.7-5.9 5.2 1.8 7.7L12 17.8 5.1 21.8l1.8-7.7L1 8.9l7.8-.7z"/></svg>On-site Inspections And Desk Review Services</li>
    <li><svg class="star" viewBox="0 0 24 24"><path d="M12 1l3.2 7.2 7.8.7-5.9 5.2 1.8 7.7L12 17.8 5.1 21.8l1.8-7.7L1 8.9l7.8-.7z"/></svg>Assessment Reports And Estimates For Repair And Restoration</li>
  </ul>

  <div class="brand">
    <div class="brand-row"><span class="brand-dot"></span><span class="brand-name">Daniel Morrow</span></div>
    <span class="brand-tag">Keystone Refinishers</span>
  </div>
</section>

<section class="card card--contact">
  <div class="backdrop" role="img" aria-label="faint soft background tint" style="left:20px;top:60px;width:200px;height:320px;background:var(--faint-blue);opacity:.7"></div>
  <div class="backdrop" role="img" aria-label="faint soft background tint" style="left:160px;top:80px;width:220px;height:300px;background:var(--faint-peach);opacity:.8"></div>
  <div class="backdrop" role="img" aria-label="faint soft background tint" style="left:120px;top:20px;width:260px;height:360px;background:var(--faint-grey);opacity:.5"></div>

  <div class="holder">
    <h1 class="holder-name">Daniel Morrow</h1>
    <p class="holder-role">Home Contents Restoration</p>
    <p class="holder-note">Serving The General Public And The insurance Industry For Over 40 Years</p>
  </div>

  <ul class="contact-list">
    <li><svg class="contact-icon" viewBox="0 0 24 24"><path d="M7 1h10a2 2 0 0 1 2 2v18a2 2 0 0 1-2 2H7a2 2 0 0 1-2-2V3a2 2 0 0 1 2-2zm0 3v14h10V4z"/></svg>555.210.4417</li>
    <li><svg class="contact-icon" viewBox="0 0 24 24"><path d="M2 9c0-4 20-4 20 0v2h-5V9H7v2H2zm4 4h12l3 8H3z"/></svg>555.318.2290</li>
    <li><svg class="contact-icon" viewBox="0 0 24 24"><path d="M6 2h9l3 3v5H6zm-3 9h18v9H3zm3 3v2h12v-2z"/></svg>555.210.4417</li>
    <li><svg class="contact-icon" viewBox="0 0 24 24"><path d="M2 5h20v14H2zm2 2v1l8 5 8-5V7l-8 5z"/></svg>studio@keystonerefinish.com</li>
    <li><svg class="contact-icon" viewBox="0 0 24 24"><path d="M12 1a7 7 0 0 1 7 7c0 5-7 15-7 15S5 13 5 8a7 7 0 0 1 7-7zm0 4a3 3 0 1 0 0 6 3 3 0 0 0 0-6z"/></svg><span>88 Cedar Hollow Rd.<br>Millbrook, Ny 10590</span></li>
  </ul>
  <div class="contact-rule"></div>

  <div class="brand">
    <div class="brand-row"><span class="brand-dot"></span><span class="brand-name">Daniel Morrow</span></div>
    <span class="brand-tag">Keystone Refinishers</span>
  </div>
</section>

</body>
</html>
```